Marrowind Vodka logo and label design

We would like a logo and bottle label design for a new line of Ultra-Premium Vodka. The Company is called Marrowind Spirits and is based in Brisbane, Australia. We would like a 'Gatsby/Prohibition era vibe to the design. We want to keep it minimalistic and sleek. We strongly prefer a minimalist design and colour palette. Black,Gold,Grey,White,Silver,Red and Blue

The bottle will be similar in shape to Halvorak/Pale Heron. There will also need to be space on the label for required information, as well as short bio of the company, which will be provided to the winning design.

We would like to add the polish code of arms for Opoczno. Have attached link for reference. https://www.crestarchive-demo.net/crestarchive/index.php?title=Opoczno

Target Market(s)

Luxury brand customers

Logo Text

Marrowind Ultra-Premium Vodka

Logo styles of interest
Wordmark Logo
Lettermark Logo
Requirements
Must have
• This is the first release from our new Vodka label. We want a logo and bottle label that reflects a premium product. We very much like Prohibition/Gatsby era themed bottles and labels. The label and bottle should be elegant and clean.
Should not have
• Anything too busy or confusing.

```html
<!DOCTYPE html>
<html lang="en">
<head>
<meta charset="utf-8">
<title>Marrowind Ultra-Premium Vodka – Label</title>
<link rel="stylesheet" href="https://fonts.googleapis.com/css2?family=Oswald:wght@500&family=Cinzel:wght@600&family=Allura&display=swap">
<style>
  :root {
    --page: #ffffff;
    --label-black: #0a0a0a;
    --gold: #c9a14e;
    --gold-light: #e8c77a;
    --gold-dark: #8a6428;
  }
  * { margin: 0; padding: 0; box-sizing: border-box; }
  html, body {
    width: 1200px;
    height: 1023px;
    overflow: hidden;
    background: var(--page);
  }
  .label {
    position: absolute;
    left: 300px;
    top: 98px;
    width: 600px;
    height: 826px;
    background: var(--label-black);
  }
  .rule {
    position: absolute;
    left: 0;
    width: 100%;
    height: 3px;
    background: linear-gradient(90deg, var(--gold-dark), var(--gold-light) 50%, var(--gold-dark));
  }
  .rule--top { top: 73px; }
  .rule--bottom { top: 750px; }
  .crest-ring {
    position: absolute;
    left: 263px;
    top: 103px;
    width: 74px;
    height: 74px;
    border: 3px solid var(--gold);
    border-radius: 50%;
  }
  .scroll-frame {
    position: absolute;
    left: 50px;
    top: 172px;
    width: 500px;
    height: 268px;
    border-radius: 60px;
    background: radial-gradient(ellipse at center, rgba(201,161,78,0.10) 0%, rgba(201,161,78,0.22) 70%, rgba(138,100,40,0.12) 100%);
  }
  .wordmark {
    position: absolute;
    left: 0;
    width: 100%;
    text-align: center;
    font-family: "Oswald", sans-serif;
    font-weight: 500;
    color: var(--gold);
  }
  .wordmark--name {
    top: 238px;
    font-size: 64px;
    letter-spacing: 9px;
    line-height: 1;
  }
  .wordmark--sub {
    top: 330px;
    font-size: 26px;
    letter-spacing: 10px;
    line-height: 1;
  }
  .grade {
    position: absolute;
    top: 470px;
    left: 0;
    width: 100%;
    text-align: center;
    font-family: "Cinzel", serif;
    font-weight: 600;
    font-size: 34px;
    letter-spacing: 1px;
    color: var(--gold);
    background: linear-gradient(90deg, var(--gold-dark), var(--gold-light) 50%, var(--gold-dark));
    -webkit-background-clip: text;
    background-clip: text;
    -webkit-text-fill-color: transparent;
  }
  .spirit {
    position: absolute;
    top: 525px;
    left: 0;
    width: 100%;
    text-align: center;
    font-family: "Allura", cursive;
    font-size: 96px;
    line-height: 1;
    color: var(--gold);
  }
  .strength {
    position: absolute;
    top: 700px;
    left: 0;
    width: 100%;
    text-align: center;
    font-family: "Oswald", sans-serif;
    font-weight: 500;
    font-size: 26px;
    letter-spacing: 1.5px;
    color: var(--gold);
  }
</style>
</head>
<body>
  <main class="label">
    <div class="rule rule--top"></div>
    <div class="crest-ring"></div>
    <div class="scroll-frame" role="img" aria-label="Ornamental gold scrollwork frame around the brand name"></div>
    <div class="wordmark wordmark--name">MARROWIND</div>
    <div class="wordmark wordmark--sub">SPIRITS</div>
    <div class="grade">Ultra-Premium</div>
    <div class="spirit">Vodka</div>
    <div class="strength">40% ALC/VOL 750ml</div>
    <div class="rule rule--bottom"></div>
  </main>
</body>
</html>
```